Interior Stylist business card design needed

I need a business card for my new company in Sydney called "Pip Dunstane Designs". The business offers an interior styling and colour consultancy. My clients are generally not very design savvy (hence why they use me) and can range from being quite conservative to really wanting something "out there". They can be looking for a budget makeover or something more expensive / substantial. I'd like my business card design to be stylish (but not overly formal). I certainly don't want it to be conservative. I'd like it to stand out a bit! I don't really have any aversion to particular colours and I don't have a logo as such - my business name is really all I have.

Target Market(s)

As above - home owners, ranging from conservative to modern

Industry/Entity Type

Conservative

Contact Information for Business Card

Pip Dunstane Designs
Colour consultancy and interior styling
ph: 0417 382 605
email: pipdunstane@harvolink.net.au

Requirements
Should not have
• Old fashioned writing or motifs. No Times Roman font!!

```html
<!DOCTYPE html>
<html lang="en">
<head>
<meta charset="utf-8">
<title>Pip Dunstane Designs – Business Card</title>
<link rel="stylesheet" href="https://fonts.googleapis.com/css2?family=Open+Sans:wdth,wght@75..100,300..800&display=swap">
<style>
  :root {
    --page-bg: #ffffff;
    --card-bg: #4b4c4e;
    --text-light: #ffffff;
    --paint-mustard: #c4a11a;
    --paint-yellow: #e2bd05;
    --paint-rust: #c7491c;
    --paint-orange: #e64304;
    --paint-teal: #1ea3bf;
    --paint-cyan: #05b7e3;
    --paint-blue: #1a6fce;
  }
  * { margin: 0; padding: 0; box-sizing: border-box; }
  html, body {
    width: 1200px;
    height: 741px;
    overflow: hidden;
    background: var(--page-bg);
  }
  .card {
    position: absolute;
    left: 0;
    top: 24px;
    width: 1200px;
    height: 692px;
    background: var(--card-bg);
    font-family: "Open Sans", Arial, sans-serif;
    color: var(--text-light);
  }
  .identity {
    position: absolute;
    left: 0;
    width: 800px;
    text-align: center;
  }
  .business-name {
    top: 224px;
    font-size: 54px;
    font-weight: 700;
    letter-spacing: 0.2px;
    line-height: 1;
  }
  .tagline {
    top: 292px;
    font-size: 27px;
    font-weight: 300;
    font-stretch: 75%;
    line-height: 1;
  }
  .contact {
    position: absolute;
    left: 0;
    width: 800px;
    text-align: center;
    font-weight: 300;
    line-height: 1;
  }
  .phone {
    top: 412px;
    font-size: 37px;
  }
  .email {
    top: 493px;
    font-size: 35px;
  }
  .paint-swatches {
    position: absolute;
    left: 703px;
    top: 36px;
    width: 497px;
    height: 603px;
  }
</style>
</head>
<body>
  <main class="card">
    <h1 class="identity business-name">Pip Dunstane Designs</h1>
    <p class="identity tagline">Colour Consultancy &amp; Interior Styling</p>

    <p class="contact phone">0417 382 605</p>
    <p class="contact email">pipdunstane@harvolink.net.au</p>

    <svg class="paint-swatches" role="img" aria-label="Brush-stroke paint swatches in mustard, yellow, orange, teal and blue" viewBox="0 0 497 603" preserveAspectRatio="none">
      <defs>
        <linearGradient id="swatch-tones" x1="0" y1="0" x2="0" y2="1">
          <stop offset="0" stop-color="var(--paint-mustard)"/>
          <stop offset="0.2" stop-color="var(--paint-yellow)"/>
          <stop offset="0.36" stop-color="var(--paint-rust)"/>
          <stop offset="0.5" stop-color="var(--paint-orange)"/>
          <stop offset="0.64" stop-color="var(--paint-teal)"/>
          <stop offset="0.82" stop-color="var(--paint-cyan)"/>
          <stop offset="1" stop-color="var(--paint-blue)"/>
        </linearGradient>
      </defs>
      <rect x="0" y="0" width="497" height="603" fill="url(#swatch-tones)"/>
    </svg>
  </main>
</body>
</html>
```